The Quiet Tide of Morning: A Path Through Silence, Courage and Light

I require designs for the front cover, rear cover and spine for a printed book. The book is the personal account of a stroke survivor.

Dimensions requested by publisher:|

Front + rear covers = 130 x 195mm with 3-5mm bleed
Spine = c. 10mm

Target Market(s)

Worldwide

Font styles to use
Decorative
Script

Requirements
Must have
• The text for the back cover (and I have attached photos for the accompanying headshot):

"Ruth Kembo had become a successful commercial lawyer in Tanzania with a professional career that spanned almost two decades. One week after celebrating her law firm’s 5th anniversary her life changed dramatically when at 4am one morning she suffered an ischaemic stroke.

After losing the use of the right side of her body and her ability to speak and swallow, Ruth was forced to undergo a full system reboot. In this brutally honest account of her life before and after the stroke Ruth describes her physical and mental battles, how she managed to accept the condition and deal with the accompanying feelings of shame.

Her story is one of rebirth, hope and ultimately transformation, offering practical advice for stroke survivors, their families and anyone embarking on a rehabilitation programme following serious illness."
Nice to have
• Modern but elegant feel. Something that signifies the metamorphosis of a butterfly, or transformation in general.

```html
<!DOCTYPE html>
<html lang="en">
<head>
<meta charset="UTF-8">
<title>The Quiet Tide of Morning – Front Cover</title>
<link rel="stylesheet" href="https://fonts.googleapis.com/css2?family=Raleway:wght@400;800&family=Pinyon+Script&display=swap">
<style>
  :root {
    --stage: #000000;
    --paper: #ffffff;
    --title-blue: #1957a6;
    --accent-red: #d1231d;
    --subtitle-magenta: #b4288c;
    --violet: #7a4aa6;
    --blue: #3a7cc8;
    --teal: #4aa8a4;
    --sun: #efd43c;
    --peach: #ee9a6a;
    --rose: #e0406e;
    --wing-violet: #6a3fa8;
    --wing-sky: #3fb0ea;
    --wing-green: #3fae4a;
    --wing-lime: #c8d83a;
    --wing-orange: #f39a2e;
    --wing-pink: #e2336a;
  }
  * { margin: 0; padding: 0; box-sizing: border-box; }
  html, body {
    width: 1200px;
    height: 1200px;
    overflow: hidden;
    background: var(--stage);
  }
  .canvas {
    position: relative;
    width: 1200px;
    height: 1200px;
    background: var(--stage);
  }
  .book-cover {
    position: absolute;
    left: 339px;
    top: 209px;
    width: 522px;
    height: 782px;
    background: var(--paper);
    overflow: hidden;
  }

  /* Watercolour stripe bands */
  .stripe-band {
    position: absolute;
    left: 0;
    width: 100%;
  }
  .stripe-band--top {
    top: 0;
    height: 150px;
    background: linear-gradient(90deg,
      var(--violet) 0%, var(--violet) 12%,
      var(--blue) 16%, var(--blue) 27%,
      var(--teal) 31%, var(--teal) 47%,
      var(--sun) 51%, var(--sun) 61%,
      var(--peach) 65%, var(--peach) 80%,
      var(--rose) 84%, var(--rose) 100%);
  }
  .stripe-band--bottom {
    bottom: 0;
    height: 144px;
    background: linear-gradient(90deg,
      var(--rose) 0%, var(--rose) 14%,
      var(--peach) 18%, var(--peach) 33%,
      var(--sun) 37%, var(--sun) 47%,
      var(--teal) 51%, var(--teal) 67%,
      var(--blue) 71%, var(--blue) 84%,
      var(--violet) 88%, var(--violet) 100%);
  }

  /* Rows of butterflies across the stripes */
  .butterfly-row {
    position: absolute;
    left: 0;
    width: 100%;
    border-radius: 40px;
  }
  .butterfly-row--top {
    top: 66px;
    height: 166px;
    background: linear-gradient(90deg,
      var(--wing-violet) 0%, var(--wing-sky) 20%, var(--wing-green) 38%,
      var(--wing-lime) 55%, var(--wing-orange) 72%, var(--wing-pink) 92%, var(--wing-violet) 100%);
  }
  .butterfly-row--bottom {
    top: 593px;
    height: 173px;
    background: linear-gradient(90deg,
      var(--wing-pink) 0%, var(--wing-orange) 18%, var(--wing-lime) 34%,
      var(--wing-green) 52%, var(--wing-sky) 72%, var(--wing-violet) 94%);
  }

  .book-title { font-weight: normal; }
  .title-line {
    position: absolute;
    left: 0;
    width: 100%;
    text-align: center;
    line-height: 1;
    white-space: nowrap;
  }
  .title-main {
    font-family: 'Raleway', sans-serif;
    font-weight: 800;
    color: var(--title-blue);
    letter-spacing: 0.5px;
  }
  .title-the { top: 239px; font-size: 52px; }
  .title-second { top: 295px; font-size: 52px; }
  .title-joiner {
    top: 340px;
    font-family: 'Pinyon Script', cursive;
    font-size: 80px;
    color: var(--accent-red);
  }
  .title-last { top: 446px; font-size: 68px; }
  .subtitle {
    position: absolute;
    left: 0;
    top: 512px;
    width: 100%;
    text-align: center;
    font-family: 'Raleway', sans-serif;
    font-weight: 400;
    font-size: 27px;
    line-height: 37px;
    letter-spacing: 0.6px;
    color: var(--subtitle-magenta);
  }
</style>
</head>
<body>
  <main class="canvas">
    <section class="book-cover" aria-label="Book front cover">
      <div class="stripe-band stripe-band--top" role="img" aria-label="Rainbow watercolour stripes"></div>
      <div class="butterfly-row butterfly-row--top" role="img" aria-label="Row of colourful butterflies in violet, blue, green, yellow, orange and pink"></div>

      <h1 class="book-title">
        <span class="title-line title-main title-the">THE</span>
        <span class="title-line title-main title-second">QUIET TIDE</span>
        <span class="title-line title-joiner">of</span>
        <span class="title-line title-main title-last">MORNING</span>
      </h1>
      <p class="subtitle">A Path Through Silence,<br>Courage and Light</p>

      <div class="stripe-band stripe-band--bottom" role="img" aria-label="Rainbow watercolour stripes"></div>
      <div class="butterfly-row butterfly-row--bottom" role="img" aria-label="Row of colourful butterflies in pink, orange, yellow, green, blue and violet"></div>
    </section>
  </main>
</body>
</html>
```